U.S. based testing, inspection, and certification (TIC) company needs a new social media design.

We need a social media design primarily for LinkedIn 1200x1200px for our U.S. based company with international capabilities for performing dozens if not hundreds of testing, inspection, and certification (TIC) services. Our primary services include calibration, chemical analysis, consulting engineering, environmental simulation, forensic engineering, materials testing, mechanical testing, and nondestructive testing. Industries we serve are aerospace/aviation, automotive, chemical, commercial properties, construction, consumer products, defense, energy storage, healthcare, insurance/legal, life science, manufacturing, oil & gas, power generation, pulp & paper, and telecommunications. https://corvintest.example/

Guideline hex colors (primary, secondary): #29aae2, #0b1f3b

The final design should communicate:
1. Trust, Integrity, and Independence
2. Technical Expertise and Accuracy
3. Efficiency and Speed
4. Value-Added Partnership

We previously used a hexagon design that we would like to part ways from; hexagon examples and QVR logos uploaded.

```html
<!DOCTYPE html>
<html lang="en">
<head>
<meta charset="utf-8">
<title>QVR — Precision You Can Count On</title>
<link rel="stylesheet" href="https://fonts.googleapis.com/css2?family=Montserrat:wght@500;700;800&family=Open+Sans:wght@400;600;700&display=swap">
<style>
  :root {
    --navy: #0b1f3b;
    --navy-panel: #123a5e;
    --navy-card: #0f2442;
    --cyan: #29aae2;
    --white: #ffffff;
    --grey: #6f7f93;
    --grey-light: #8a97a8;
    --line: #2d4a6b;
  }
  * { margin: 0; padding: 0; box-sizing: border-box; }
  html, body { width: 1200px; height: 1200px; overflow: hidden; background: var(--navy); }
  .canvas {
    position: relative; width: 1200px; height: 1200px;
    background: var(--navy); color: var(--white);
    font-family: "Montserrat", sans-serif; overflow: hidden;
  }
  .top-band { position: absolute; left: 0; top: 0; width: 100%; height: 15px; background: var(--cyan); }

  .brand { position: absolute; left: 80px; top: 52px; display: flex; flex-direction: column; gap: 4px; }
  .brand-name { display: flex; align-items: center; gap: 16px; font-family: "Montserrat", sans-serif; font-weight: 800; font-size: 78px; line-height: 1; letter-spacing: 4px; color: var(--white); }
  .brand-mark { width: 22px; height: 22px; background: var(--white); }
  .brand-full { font-family: "Open Sans", sans-serif; font-size: 23px; color: var(--white); margin-top: 6px; }

  .tagline-box {
    position: absolute; left: 714px; top: 124px; width: 407px; height: 39px;
    border: 1.5px solid var(--cyan); color: var(--cyan);
    font-family: "Open Sans", sans-serif; font-size: 20px; letter-spacing: 1px;
    display: flex; align-items: center; justify-content: center;
  }
  .rule { position: absolute; left: 80px; width: 1041px; height: 1px; background: var(--cyan); opacity: .7; }
  .rule-top { top: 206px; }
  .rule-mid { top: 645px; background: var(--line); opacity: 1; }

  .hero-photo {
    position: absolute; left: 0; top: 257px; width: 460px; height: 335px;
    background: linear-gradient(135deg, #dfe9f2 0%, #b7c9d9 45%, #8aa2b8 70%, #d8e3ec 100%);
  }
  .accent-bar { position: absolute; left: 460px; top: 239px; width: 38px; height: 369px; background: var(--cyan); }

  .headline {
    position: absolute; left: 550px; top: 268px;
    font-weight: 800; font-size: 95px; line-height: 85px; letter-spacing: 1px;
  }
  .headline span { display: block; }
  .headline .accent { color: var(--cyan); }
  .subhead {
    position: absolute; left: 554px; top: 541px;
    font-family: "Open Sans", sans-serif; font-size: 29px; letter-spacing: 2.5px; color: var(--grey);
  }

  .stats { position: absolute; left: 80px; top: 668px; width: 1041px; height: 115px; display: flex; }
  .stat { width: 260px; position: relative; padding-left: 0; }
  .stat + .stat { padding-left: 26px; }
  .stat + .stat::before { content: ""; position: absolute; left: 0; top: 6px; width: 2px; height: 106px; background: var(--line); }
  .stat-value { font-weight: 800; font-size: 70px; line-height: 66px; color: var(--cyan); letter-spacing: -1px; }
  .stat-label { font-family: "Open Sans", sans-serif; font-size: 15px; line-height: 20px; color: var(--grey); margin-top: 12px; }

  .services {
    position: absolute; left: 80px; top: 822px; width: 1041px; height: 174px;
    display: grid; grid-template-columns: 1fr 1fr; grid-template-rows: repeat(3, 1fr);
    border: 2px solid var(--cyan); background: var(--navy-panel);
  }
  .service {
    display: flex; align-items: center; justify-content: center;
    font-family: "Montserrat", sans-serif; font-weight: 500; font-size: 20px; letter-spacing: 2px;
    border-bottom: 2px solid var(--cyan);
  }
  .service:nth-child(odd) { border-right: 2px solid var(--cyan); }
  .service:nth-last-child(-n+2) { border-bottom: none; }

  .values { position: absolute; left: 80px; top: 1042px; width: 1041px; height: 59px; display: flex; border: 2px solid #1c3350; background: var(--navy-card); }
  .value { flex: 1; display: flex; align-items: center; gap: 10px; padding-left: 17px; }
  .value + .value { border-left: 2px solid #1c3350; }
  .value svg { width: 32px; height: 32px; flex: none; }
  .value-title { font-family: "Open Sans", sans-serif; font-weight: 700; font-size: 11px; line-height: 13px; }
  .value-note { font-family: "Open Sans", sans-serif; font-size: 8.5px; line-height: 11px; color: var(--grey-light); }

  .footer-rule { position: absolute; left: 0; top: 1137px; width: 100%; height: 1px; background: var(--line); }
  .footer-url { position: absolute; left: 80px; top: 1160px; font-family: "Open Sans", sans-serif; font-size: 12px; letter-spacing: 1px; color: var(--grey-light); }
  .footer-slogan { position: absolute; right: 67px; top: 1160px; font-family: "Montserrat", sans-serif; font-weight: 700; font-size: 13px; color: var(--cyan); }
</style>
</head>
<body>
<main class="canvas">
  <div class="top-band"></div>

  <header class="brand">
    <div class="brand-name"><span class="brand-mark"></span>QVR</div>
    <div class="brand-full">Quantum Verification Resources</div>
  </header>
  <div class="tagline-box">TIC Services · U.S. Based · Global Reach</div>
  <div class="rule rule-top"></div>

  <div class="hero-photo" role="img" aria-label="Gloved hand placing a polished calibration weight on a laboratory balance"></div>
  <div class="accent-bar"></div>

  <h1 class="headline">
    <span>PRECISION</span>
    <span class="accent">YOU CAN</span>
    <span>COUNT ON.</span>
  </h1>
  <p class="subhead">TESTING · INSPECTION · CERTIFICATION</p>

  <div class="rule rule-mid"></div>

  <section class="stats">
    <div class="stat"><div class="stat-value">100+</div><div class="stat-label">Distinct TIC<br>Services</div></div>
    <div class="stat"><div class="stat-value">16+</div><div class="stat-label">Industries<br>Served</div></div>
    <div class="stat"><div class="stat-value">50+</div><div class="stat-label">Years of<br>Experience</div></div>
    <div class="stat"><div class="stat-value">IAQB</div><div class="stat-label">Accredited<br>Laboratory</div></div>
  </section>

  <section class="services">
    <div class="service">TESTING</div>
    <div class="service">FORENSICS</div>
    <div class="service">INSPECTION</div>
    <div class="service">ENGINEERING</div>
    <div class="service">CALIBRATION</div>
    <div class="service">TRAINING</div>
  </section>

  <section class="values">
    <div class="value">
      <svg viewBox="0 0 32 32" fill="none" stroke="#29aae2" stroke-width="1.3"><circle cx="16" cy="16" r="14.5"/><path d="M10.5 16.5l4 4 7.5-9"/></svg>
      <div><div class="value-title">Independent</div><div class="value-note">Unbiased Result</div></div>
    </div>
    <div class="value">
      <svg viewBox="0 0 32 32" fill="none" stroke="#29aae2" stroke-width="1.3"><rect x="1.5" y="1.5" width="29" height="29"/><path d="M16 5v22M5 16h22"/></svg>
      <div><div class="value-title">Accurate</div><div class="value-note">Certified Data</div></div>
    </div>
    <div class="value">
      <svg viewBox="0 0 32 32" fill="none" stroke="#29aae2" stroke-width="1.3"><circle cx="16" cy="16" r="14.5"/><path d="M16 8v8l5 4"/></svg>
      <div><div class="value-title">Efficient</div><div class="value-note">Fast Turnaround</div></div>
    </div>
    <div class="value">
      <svg viewBox="0 0 32 32" fill="none" stroke="#29aae2" stroke-width="1.3"><circle cx="16" cy="16" r="14.5"/><path d="M9 20l5-5 3 3 6-7"/></svg>
      <div><div class="value-title">Trusted Partner</div><div class="value-note">End-to-End Value</div></div>
    </div>
  </section>

  <div class="footer-rule"></div>
  <div class="footer-url">www.corvintest.example</div>
  <div class="footer-slogan">FROM CONFIDENCE TO CERTAINTY</div>
</main>
</body>
</html>
```